Package/Product Design: Fullora 100% Scalp Coverage Powders

Need to design "high style" box and product disc design. Open to any and all suggestions. We sell 800+ skus a month on Marketvale and looking to take our box design to the next level so that we can sell even more with new look. Our competition is https://www.brevano.com/ and https://www.quillsy.com/ I know Brevano has a ton of money,,, but their products look "high touch, high style" and that is what we are going after. The compact has to have the ingredients on the back, same as the box. So looking for a design that makes the packaging look sleek, and still gets out point across. Logo should be in White or Black.

Target Market(s)

We sell to individuals who are experiencing hair loss, thinning hair, or gray/balding hair. This product creates the illusion of hair and allows clients get gain back confidence.

We sell on Marketvale (search fullora or scalp concealer), and www.fullorahairdust.com

Industry/Entity Type

Hair And Beauty

Logo Text

Fullora 100% Scalp Coverage Powders

Colors

Designer to choose colors to be used in the design.

Requirements
Must have
• Quality/high touch/high feel look to the packaging. Open to any and all suggestions.

```html
<!DOCTYPE html>
<html lang="en">
<head>
<meta charset="utf-8">
<title>Fullora Hair Powder – Box Panels</title>
<link rel="stylesheet" href="https://fonts.googleapis.com/css2?family=Oswald:wght@500&family=Source+Code+Pro:wght@400;600;700&family=Inter:wght@400;600&display=swap">
<style>
  :root {
    --backdrop: #d4d4d4;
    --panel-white: #ffffff;
    --panel-shade: #eeeeee;
    --charcoal: #2b2b2b;
    --side-dark: #303030;
    --ink: #3a3a3a;
    --badge-green: #7f8f35;
    --badge-ring: #c9d29a;
    --direction-green: #8a9a3c;
    --text-light: #ffffff;
    --text-muted: #c9c9c9;
    --swatch-blonde: #7a5a3a;
    --swatch-light-brown: #6e4d35;
    --swatch-dark-brown: #4c3b2d;
    --swatch-black: #2a2a26;
    --swatch-auburn: #7a3e22;
  }
  * { margin: 0; padding: 0; box-sizing: border-box; }
  html, body { width: 1200px; height: 1050px; overflow: hidden; background: var(--backdrop); }

  /* ---------- side panel ---------- */
  .box-side {
    position: absolute; left: 100px; top: 5px; width: 200px; height: 1040px;
    background: linear-gradient(180deg, #383838 0%, var(--side-dark) 100%);
    overflow: hidden;
  }
  .side-label {
    position: absolute; left: 6px; top: 330px;
    writing-mode: vertical-rl; white-space: nowrap;
    font-family: "Source Code Pro", monospace; font-size: 15px; letter-spacing: 3px;
    color: var(--text-light);
  }
  .directions-frame {
    position: absolute; left: 32px; top: 55px; width: 112px; height: 940px;
    border: 2px solid var(--direction-green);
    padding: 14px 10px;
  }
  .directions {
    writing-mode: vertical-rl; height: 100%;
    font-family: "Inter", sans-serif; font-size: 21px; line-height: 27px;
    color: var(--direction-green);
  }
  .directions strong { font-weight: 600; display: block; }
  .side-brand {
    position: absolute; left: 150px; top: 300px;
    writing-mode: vertical-rl; white-space: nowrap;
    font-family: "Source Code Pro", monospace; font-weight: 700; font-size: 40px;
    letter-spacing: 2px; color: var(--text-muted);
  }
  .side-tagline {
    position: absolute; left: 128px; top: 315px;
    writing-mode: vertical-rl; white-space: nowrap;
    font-family: "Source Code Pro", monospace; font-size: 14px; letter-spacing: 4px;
    color: var(--text-muted);
  }

  /* ---------- front panel ---------- */
  .box-front {
    position: absolute; left: 300px; top: 5px; width: 840px; height: 1040px;
    background: linear-gradient(180deg, var(--panel-white) 0%, var(--panel-shade) 100%);
    overflow: hidden;
    font-family: "Source Code Pro", monospace;
    color: var(--ink);
  }
  .dark-base { position: absolute; left: 0; top: 0; width: 840px; height: 1040px; }
  .brand-name {
    position: absolute; top: 135px; left: 0; width: 100%; text-align: center;
    font-weight: 700; font-size: 158px; letter-spacing: 4px; line-height: 1;
    color: var(--ink); white-space: nowrap;
  }
  .tagline {
    position: absolute; top: 290px; left: 0; width: 100%; text-align: center;
    font-size: 40px; letter-spacing: 8px; color: var(--ink); white-space: nowrap;
  }
  .swatches {
    position: absolute; top: 405px; left: 0; width: 100%;
    display: flex; justify-content: center; gap: 38px;
  }
  .swatch {
    width: 50px; height: 50px; border-radius: 50%;
    border: 3px solid #e3e3e3; box-shadow: 0 0 0 1px #9a9a9a;
  }
  .swatch.blonde { background: var(--swatch-blonde); }
  .swatch.light-brown { background: var(--swatch-light-brown); }
  .swatch.dark-brown { background: var(--swatch-dark-brown); }
  .swatch.black { background: var(--swatch-black); }
  .swatch.auburn { background: var(--swatch-auburn); }
  .product-type {
    position: absolute; top: 520px; left: 158px; width: 557px; height: 105px;
    border: 2px solid var(--ink);
    display: flex; align-items: center; justify-content: center;
    white-space: nowrap;
    font-size: 50px; font-weight: 600; letter-spacing: 16px; padding-left: 16px;
  }
  .connector { position: absolute; top: 625px; left: 446px; width: 2px; height: 48px; background: var(--ink); }
  .talc-free {
    position: absolute; top: 670px; left: 0; width: 100%; text-align: center;
    font-size: 46px; font-weight: 600; letter-spacing: 2px; white-space: nowrap;
  }
  .badge {
    position: absolute; width: 150px; height: 150px; border-radius: 50%;
    background: var(--badge-green); border: 4px solid var(--badge-ring);
    display: flex; align-items: center; justify-content: center; text-align: center;
    font-family: "Oswald", sans-serif; font-weight: 500; font-size: 22px; line-height: 1.2;
    color: var(--text-light); text-transform: uppercase;
  }
  .badge.coverage { left: 157px; top: 775px; }
  .badge.bald-spots { left: 370px; top: 765px; }
  .badge.waterproof { left: 575px; top: 755px; }
  .net-weight {
    position: absolute; top: 945px; left: 0; width: 100%; text-align: center;
    font-size: 40px; color: var(--text-light); letter-spacing: 1px; white-space: nowrap;
  }
</style>
</head>
<body>
  <section class="box-side">
    <div class="side-label">HAIR POWDER | TALC-FREE</div>
    <div class="directions-frame">
      <p class="directions"><strong>Directions:</strong>In a circular motion, rub applicator brush around the pressed powder. Lightly apply to desired area directly on the scalp using small round strokes. Repeat until proper coverage is obtained.</p>
    </div>
    <div class="side-tagline">100% Scalp Coverage</div>
    <div class="side-brand">FULLORA</div>
  </section>

  <section class="box-front">
    <svg class="dark-base" viewBox="0 0 840 1040" aria-hidden="true">
      <path d="M0 785 C 150 820, 280 845, 380 842 C 520 838, 680 770, 840 695 L 840 1040 L 0 1040 Z" fill="var(--charcoal)"/>
    </svg>
    <div class="brand-name">FULLORA</div>
    <div class="tagline">100% Scalp Coverage</div>
    <div class="swatches">
      <span class="swatch blonde"></span>
      <span class="swatch light-brown"></span>
      <span class="swatch dark-brown"></span>
      <span class="swatch black"></span>
      <span class="swatch auburn"></span>
    </div>
    <div class="product-type">HAIR POWDER</div>
    <div class="connector"></div>
    <div class="talc-free">TALC-FREE</div>
    <div class="badge coverage">100%<br>Instant<br>Coverage</div>
    <div class="badge bald-spots">Fillsin<br>Bald Spots</div>
    <div class="badge waterproof">Waterproof<br>Easy to Apply</div>
    <div class="net-weight">Net Wt.32OZ/9G</div>
  </section>
</body>
</html>
```